Dental Lab Delivery Box Design 163x115x97mm

* AI file of the box attached
* Full-Color outside and one color inside
* Return pictures of the 3D design; so we can have a better idea of how it will turn out
* Match Logo Color and Design
* Please find attached Words doc for the wording
* Research the dental lab delivery
* Attached our sister lab dental lab design
*
Updates

Thank for designing! We are reviewing and asking designers for improvements. We have extended the due date! More designs welcome!

Target Market(s)

Dental Office

Industry/Entity Type

Dental Lab

Font styles to use
Serif

Colors
0054AA
0677BA
7BADD7
CADEEF
E8F1F8

Requirements
Must have
• Advance, Clean, and Matched Logo color
Nice to have
• Graphics
Should not have
• Too much words or over advertise

```html
<!DOCTYPE html>
<html lang="en">
<head>
<meta charset="utf-8">
<title>Veltra Dental Inc – Delivery Box</title>
<link rel="stylesheet" href="https://fonts.googleapis.com/css2?family=Montserrat:wght@600&family=Dancing+Script:wght@500&display=swap">
<style>
  :root {
    --bg: #e4e4e4;
    --panel: #ffffff;
    --navy: #1f4a8e;
    --navy-dark: #193d76;
    --brand-blue: #0054aa;
    --wave-blue: #7badd7;
    --wave-light: #cadeef;
    --wave-pale: #e8f1f8;
    --ink-grey: #6f6f6f;
    --side-grey: #c9ccd3;
  }
  * { margin: 0; padding: 0; box-sizing: border-box; }
  html, body { width: 1200px; height: 1200px; overflow: hidden; }
  body { background: var(--bg); position: relative; }

  .box-layout { position: absolute; left: 72px; top: 197px; width: 1056px; height: 806px; }

  .lid-panel {
    position: absolute; left: 0; top: 0; width: 619px; height: 437px;
    background: var(--panel); overflow: hidden;
  }
  .lid-band { position: absolute; top: 0; width: 34px; height: 100%; background: var(--navy); }
  .lid-band--left { left: 0; }
  .lid-band--right { right: 0; }

  .wave-graphic {
    position: absolute; left: 34px; right: 34px; bottom: 0; height: 230px;
    background:
      radial-gradient(ellipse 70% 60% at 30% 100%, rgba(6,119,186,0.45), transparent 70%),
      linear-gradient(170deg, transparent 25%, var(--wave-light) 55%, var(--wave-blue) 80%, var(--wave-pale) 100%);
    clip-path: polygon(0 0, 12% 0, 30% 45%, 60% 55%, 100% 75%, 100% 100%, 0 100%);
  }

  .brand-name {
    position: absolute; top: 96px; left: 0; right: 0; text-align: center;
    font-family: "Montserrat", sans-serif; font-weight: 600;
    font-size: 38px; letter-spacing: 3px; color: var(--brand-blue);
    line-height: 1.1;
  }
  .brand-name .brand-sub { display: block; font-size: 20px; letter-spacing: 8px; }

  .front-panel {
    position: absolute; left: 0; top: 437px; width: 619px; height: 369px;
    background: var(--panel); border-top: 1px solid #ececec;
    display: flex; align-items: center; justify-content: center;
  }
  .tagline {
    font-family: "Dancing Script", cursive; font-weight: 500;
    font-size: 40px; letter-spacing: 6px; color: var(--ink-grey);
  }

  .side-panel {
    position: absolute; left: 619px; top: 437px; width: 437px; height: 369px;
    background: linear-gradient(180deg, var(--navy), var(--navy-dark));
    display: flex; align-items: center; justify-content: center;
  }
  .side-panel .brand-name {
    position: static; color: var(--side-grey); font-size: 34px;
  }
  .side-panel .brand-name .brand-sub { font-size: 18px; }
</style>
</head>
<body>
  <div class="box-layout">
    <section class="lid-panel">
      <div class="lid-band lid-band--left"></div>
      <div class="lid-band lid-band--right"></div>
      <div class="wave-graphic" role="img" aria-label="Flowing translucent blue wave graphic across the lid"></div>
      <p class="brand-name">VELTRA<span class="brand-sub">DENTAL INC</span></p>
    </section>

    <section class="front-panel">
      <p class="tagline">Lab with Confidence</p>
    </section>

    <section class="side-panel">
      <p class="brand-name">VELTRA<span class="brand-sub">DENTAL INC</span></p>
    </section>
  </div>
</body>
</html>
```